International sports trophy business needs a web design

We need two pages designed for a new company called medalnook. We sell innovative sports trophies via our website and store details of past purchases to allow returning customers to easily place their orders. Customers can log into their accounts using chatterlane or a secondary account login button. The final design should be clean and should focus on the theme of winning the trophy as it is applicable to all sports.

The page should be designed with themes that can be used throughout the site that we'll turn into a cms theme.
Updates

Hi All,

We're half way in to the competition now and I thought it'd be a good time to provide an update on how things are progressing.  First let me thank you for taking part, there's some really great ideas happening here however some of you have requested a mockup for the second page.  I've put that up now and you should be able to find it in the files section of the brief.  Hopefully this will give people a better starting point than before.

To everybody who is still waiting for feedback, be patient, I'm currently working my way through the designs and will be in contact shortly.  I thought in the meantime I could provide a general update as to how I think the competition is progressing and the concepts that I like the most so far. 

For the landing page... The designs that are leading at the moment are not busy or crowded and devote most of the page layout to the front page info-graphic.  The logo, login and primary menu are all easy to identify but not where your eye lands when viewing the page.  The copyright information and secondary menus are there if you look for them.  As far as the style goes we've found that some of the designs feel a little too serious and too adult and we'd like a more playful feel, if you think that your design already is playful, then we probably do too.  Finally I'll add that we like our logo, but that doesn't mean that we want to see it more than once on the landing page (it's pointless and designs that do this will be unlikely to win) and we certainly do not want to see people creating a new logo or changing our name to nook medal.

For the trophy sales page... There are fewer designs done to this specification as some are unwilling to invest the time in design or unwilling to work without a mockup.  The mockup has now been uploaded to the site (we did want to see what kind of ideas would come here if we didn't include one, thanks to those who had a shot).  If you have any other query about the sales page feel free to contact us.

A final general comment, we want to make sure that all of the images used in your designs are not infringing copyright (this includes images in our mockups, we can only guarantee that we own the copyright for the medalnook logo.).

Hi all, the sliders below have been updated to reflect the more playful design feel that we prefer so far.

Target Market(s)

Our target market is sporting and youth focused but must be adult friendly.

Industry/Entity Type

Business

Requirements
Must have
• We want two pages designed, a landing page and a product display page. We would like a common border scheme across both showing the logo (attached) in the top corner, and secondary links along the bottom.

Landing Page - Must Haves

We see trophies as a representation of achievement and something that can be shared with friends and family. We would like to convey this message in a graphic or illustration on the landing page. Currently in the mockup we have a bunch of trophies, this should not be the final image here.

We have attached a wireframe for the basic format that we'd like to see, you're free to expand upon this as you see fit.

Product Display Page - Must Haves

The product display page will feature a coverflow type device that holds images of the available trophies. It should show the category of the trophy, in this case choose a specific sport to feature (up to you). There should be space for the details of the trophy including price, dimensions, product name, product code, material. There should be room on the page for advertising, this will be common throughout the site except for the landing page. You should include buttons to allow you to add the trophy to your shopping cart and a shopping cart graphic somewhere on the page. There should be a menu bar, unique to this page, that allows a user to choose a new trophy to buy, view previous purchases, view current cart and account settings.

Should not have
• The design should be sport neutral, so don't focus on a single sport or category of sports or sports particular to a certain nationality. With that it's probably easier to just focus on the trophy and achievement aspect rather than the sport being played.

```html
<!DOCTYPE html>
<html lang="en">
<head>
<meta charset="utf-8">
<title>medalnook – Star Quarterback Trophy</title>
<link rel="stylesheet" href="https://fonts.googleapis.com/css2?family=Arimo:wght@400;700&display=swap">
<style>
  :root {
    --page-bg: #ffffff;
    --frame-line: #c9c9c9;
    --header-top: #ffffff;
    --header-bottom: #e4e4e4;
    --nav-red-top: #a3001c;
    --nav-red-bottom: #5c000c;
    --nav-black-top: #3a3a3a;
    --nav-black-bottom: #050505;
    --nav-divider: #c45061;
    --banner-bg: #dcdcdc;
    --text-dark: #333333;
    --text-mid: #555555;
    --price: #a8002e;
    --panel-line: #d4d4d4;
    --box-line: #dadada;
    --avatar-frame: #c8c8e6;
    --avatar-fill: #d4d4d4;
    --photo-light: #f3efea;
    --photo-dark: #6a5038;
    --base-light: #e6e6e6;
    --base-dark: #1e1e1e;
  }
  * { box-sizing: border-box; margin: 0; padding: 0; }
  html, body {
    width: 1200px; height: 938px; overflow: hidden;
    background: var(--page-bg);
    font-family: "Arimo", Arial, sans-serif;
    color: var(--text-dark);
  }
  .site {
    position: absolute; left: 39px; top: 20px; width: 1122px; height: 900px;
    border: 1px solid var(--frame-line);
  }
  .site-header {
    position: absolute; left: 0; top: 0; width: 100%; height: 134px;
    background: linear-gradient(var(--header-top) 45%, var(--header-bottom));
    border-bottom: 1px solid var(--frame-line);
  }
  .brand {
    position: absolute; left: 16px; top: 50px;
    display: flex; align-items: center; gap: 12px;
    font-size: 30px; font-weight: 400; letter-spacing: 3px; color: #222;
  }
  .brand-mark { width: 34px; height: 34px; border-radius: 50%; background: var(--nav-red-top); }
  .avatar {
    position: absolute; left: 945px; top: 0; width: 121px; height: 97px;
    background: #eeeef8; border: 1px solid var(--avatar-frame);
    box-shadow: 2px 3px 5px rgba(0,0,0,.25);
    display: flex; align-items: center; justify-content: center;
  }
  .avatar-inner { width: 90px; height: 70px; background: #fff; display: flex; align-items: flex-end; justify-content: center; }

  .main-nav {
    position: absolute; left: 1px; top: 137px; width: 932px; height: 47px;
    display: flex;
    background: linear-gradient(var(--nav-red-top), var(--nav-red-bottom));
    box-shadow: 0 2px 2px rgba(0,0,0,.2);
  }
  .main-nav a {
    display: flex; align-items: center; justify-content: center;
    color: #fff; text-decoration: none; font-weight: 700; font-size: 16px;
    border-right: 1px solid var(--nav-divider);
  }
  .main-nav a.is-current { background: linear-gradient(var(--nav-black-top), var(--nav-black-bottom)); }

  .ad-banner {
    position: absolute; left: 934px; top: 136px; width: 187px; height: 713px;
    background: var(--banner-bg);
    display: flex; align-items: center; justify-content: center;
    font-size: 13px; font-weight: 700; color: #333;
  }

  .coverflow { position: absolute; left: 0; top: 190px; width: 933px; height: 440px; }
  .coverflow svg { position: absolute; left: 0; top: 0; }
  .featured-card {
    position: absolute; left: 282px; top: 46px; width: 368px; height: 382px;
    background: #fff; border: 1px solid var(--panel-line);
    box-shadow: 0 4px 6px rgba(0,0,0,.08);
  }
  .featured-photo {
    position: absolute; left: 22px; top: 42px; width: 330px; height: 282px;
    background: radial-gradient(ellipse at 45% 55%, var(--photo-dark) 0 30%, #a89680 48%, var(--photo-light) 72%);
  }
  .featured-title {
    position: absolute; left: 0; bottom: 18px; width: 100%; text-align: center;
    font-size: 21px; color: #111;
  }

  .info-box {
    position: absolute; top: 634px; width: 238px; height: 198px;
    border: 1px solid var(--box-line); border-radius: 18px;
    background: linear-gradient(#fff 70%, #f2f2f2);
    box-shadow: 0 1px 3px rgba(0,0,0,.1);
  }
  .info-box h2 { font-size: 12px; font-weight: 700; color: var(--text-mid); text-align: center; margin-top: 19px; }
  .bases { left: 20px; }
  .base-grid { display: grid; grid-template-columns: 76px 76px; gap: 24px 28px; justify-content: center; margin-top: 14px; }
  .base { height: 50px; border-radius: 8px; }
  .base.light { background: linear-gradient(160deg, #fafafa, var(--base-light) 60%, #b9b9b9); }
  .base.dark { background: linear-gradient(160deg, #555, var(--base-dark) 60%, #000); }

  .engraving { left: 675px; }
  .engraving-field {
    position: absolute; left: 23px; top: 52px; width: 190px; height: 124px;
    border: 1px solid #ccc; box-shadow: inset 1px 1px 3px rgba(0,0,0,.15);
    padding: 14px 16px; font-size: 12px; line-height: 18px; color: #333;
  }

  .product-details {
    position: absolute; left: 330px; top: 652px; width: 260px; text-align: center;
    font-weight: 700; font-size: 15px; color: var(--text-mid); line-height: 26px;
  }
  .product-price { font-size: 24px; color: var(--price); line-height: 26px; }
  .add-to-cart {
    position: absolute; left: 366px; top: 769px; width: 188px; height: 42px;
    background: linear-gradient(var(--nav-red-top), var(--nav-red-bottom));
    color: #fff; font-weight: 700; font-size: 19px; border: 0;
    display: flex; align-items: center; justify-content: center; gap: 8px;
    box-shadow: 2px 3px 5px rgba(0,0,0,.3); font-family: inherit;
  }

  .site-footer {
    position: absolute; left: 0; bottom: 0; width: 100%; height: 50px;
    border-top: 1px solid var(--frame-line);
    background: linear-gradient(#fff, #e9e9e9);
    font-size: 12px; color: #222;
  }
  .copyright { position: absolute; left: 17px; top: 19px; }
  .footer-links { position: absolute; right: 15px; top: 20px; display: flex; gap: 10px; }
  .footer-links a { color: #222; text-decoration: none; }
</style>
</head>
<body>
<div class="site">
  <header class="site-header">
    <div class="brand"><span class="brand-mark"></span><span>MEDALNOOK</span></div>
    <div class="avatar" aria-label="Account login">
      <div class="avatar-inner">
        <svg width="56" height="58" viewBox="0 0 56 58"><circle cx="28" cy="17" r="12" fill="var(--avatar-fill)"/><path d="M4 58 Q4 32 28 32 Q52 32 52 58 Z" fill="var(--avatar-fill)"/></svg>
      </div>
    </div>
  </header>

  <nav class="main-nav">
    <a class="is-current" href="#" style="width:85px">Home</a>
    <a href="#" style="width:96px">Sport</a>
    <a href="#" style="width:185px">Previous Purchases</a>
    <a href="#" style="width:136px">My Account</a>
    <a href="#" style="width:98px;border-right:0">My Cart</a>
  </nav>

  <aside class="ad-banner">Banner</aside>

  <section class="coverflow">
    <svg width="933" height="440" viewBox="0 0 933 440">
      <defs>
        <linearGradient id="fade" x1="0" y1="0" x2="0" y2="1">
          <stop offset="0" stop-color="#eeeeee"/><stop offset="1" stop-color="#fff"/>
        </linearGradient>
      </defs>
      <g fill="#fff" stroke="var(--panel-line)" stroke-width="1.2">
        <polygon points="9,74 96,116 96,368 9,395"/>
        <polygon points="96,74 204,120 204,365 96,380"/>
        <polygon points="204,74 282,100 282,355 204,368"/>
        <polygon points="650,100 727,74 727,368 650,355"/>
        <polygon points="727,120 835,74 835,380 727,365"/>
        <polygon points="835,116 922,74 922,395 835,368"/>
      </g>
      <g fill="url(#fade)" opacity=".8">
        <polygon points="9,395 96,368 96,430 9,430"/>
        <polygon points="96,380 282,355 282,430 96,430"/>
        <polygon points="650,355 835,380 835,430 650,430"/>
        <polygon points="835,368 922,395 922,430 835,430"/>
      </g>
    </svg>
    <div class="featured-card">
      <div class="featured-photo" role="img" aria-label="Photo of a bronzed football player figurine running with the ball on a black base"></div>
      <p class="featured-title">Star Quarterback Trophy</p>
    </div>
  </section>

  <section class="info-box bases">
    <h2>Available Bases</h2>
    <div class="base-grid">
      <div class="base light" role="img" aria-label="White marble base"></div>
      <div class="base light" role="img" aria-label="Grey marble base"></div>
      <div class="base dark" role="img" aria-label="Black base"></div>
      <div class="base dark" role="img" aria-label="Black marble base with gold veins"></div>
    </div>
  </section>

  <section class="product-details">
    <p>Star Quarterback Trophy</p>
    <p>PC:1456342</p>
    <p>150mm Bronzed Figurine</p>
    <p class="product-price">$10.50</p>
  </section>
  <button class="add-to-cart">Add to Cart
    <svg width="20" height="18" viewBox="0 0 20 18"><path d="M1 2h3l2.5 9h9.5l2-7H6" fill="none" stroke="#fff" stroke-width="2"/><circle cx="8" cy="15" r="1.8" fill="#fff"/><circle cx="15" cy="15" r="1.8" fill="#fff"/></svg>
  </button>

  <section class="info-box engraving">
    <h2>Enter the text for your award</h2>
    <div class="engraving-field">Lorem ipsum dolor sit amet consecutor. Lorem ipsum dolor sit amet consecutor.</div>
  </section>

  <footer class="site-footer">
    <span class="copyright">Copyright © 2011</span>
    <nav class="footer-links">
      <a href="#">About</a><span>I</span><a href="#">Privacy Policy</a><span>I</span><a href="#">Terms of Service</a><span>I</span><a href="#">Help</a>
    </nav>
  </footer>
</div>
</body>
</html>
```